TalkBridge - Language Coaching Services

Sleek, innovative, trendy design for Language Coaching business.

TalkBridge is a new UK based company that provides Language Coaching services. We offer highly personalized on-line and face to face language courses. We also impart learning techniques workshops based on the latest neuroscience research for second-language acquisition.

Target Market(s)

Industry/Entity Type

Consulting

Contact Information for Business Card

TalkBridge
ElenaVT@talkbridge-demo.co.uk
TalkBridge-demo.co.uk
London, UK

Font styles to use
Sans Serif

```html
<!DOCTYPE html>
<html lang="en">
<head>
<meta charset="UTF-8">
<title>TalkBridge Business Card</title>
<link href="https://fonts.googleapis.com/css2?family=Roboto:ital,wght@0,300;0,400;0,500;0,700;1,400&family=Roboto+Condensed:ital,wght@0,400;1,400&display=swap" rel="stylesheet">
<style>
  :root {
    --bg: #e6e8ea;
    --card-light: #f7f7f7;
    --card-dark: #262829;
    --ink: #3a3d40;
    --ink-soft: #6a6e72;
    --brand-deep: #0a6aa6;
    --brand-bright: #1d9fd9;
    --on-dark: #d9dbdd;
    --rule-dark: #5a5d60;
  }
  * { margin: 0; padding: 0; box-sizing: border-box; }
  html, body { width: 1200px; height: 900px; overflow: hidden; }
  body {
    background: var(--bg);
    font-family: "Roboto", sans-serif;
    display: flex; flex-direction: column; align-items: center; justify-content: center;
    gap: 40px;
  }
  .card {
    width: 700px; height: 400px; border-radius: 22px; position: relative; overflow: hidden;
    box-shadow: 0 10px 30px rgba(0,0,0,.18);
  }
  /* Front */
  .card-front { background: linear-gradient(135deg, #ffffff 0%, var(--card-light) 60%, #eaeaea 100%); }
  .person { position: absolute; left: 48px; top: 60px; }
  .person-name { font-weight: 700; font-size: 30px; letter-spacing: 1px; color: var(--brand-deep); text-transform: uppercase; }
  .person-name .surname { color: var(--brand-bright); font-weight: 500; }
  .person-role { font-size: 18px; color: var(--ink-soft); margin-top: 2px; }
  .contact { position: absolute; left: 48px; top: 170px; font-size: 18px; color: var(--ink); line-height: 1.55; letter-spacing: .5px; }
  .contact-row { display: flex; align-items: center; gap: 10px; }
  .contact-row svg { width: 14px; height: 14px; fill: var(--ink-soft); flex: none; }
  .contact-row.plain { padding-left: 24px; }
  .contact .web-strong { color: var(--brand-deep); font-weight: 700; }
  .divider { position: absolute; left: 48px; right: 48px; top: 145px; height: 2px; background: var(--brand-deep); }
  .brand { position: absolute; right: 56px; top: 230px; display: flex; align-items: center; gap: 14px; }
  .brand-dot { width: 46px; height: 46px; border-radius: 50%; background: var(--brand-deep); }
  .brand-name { font-size: 40px; font-weight: 500; color: var(--brand-deep); letter-spacing: 1px; }
  /* Back */
  .card-back { background: var(--card-dark); color: var(--on-dark); text-align: center; }
  .back-brand { display: flex; align-items: center; justify-content: center; gap: 16px; margin-top: 50px; }
  .back-brand .brand-name { font-size: 46px; font-weight: 300; color: var(--brand-deep); }
  .back-brand .brand-dot { width: 52px; height: 52px; }
  .services-title { font-size: 30px; color: var(--brand-deep); font-weight: 500; margin-top: 26px; }
  .tagline { font-family: "Roboto Condensed", sans-serif; font-style: italic; font-size: 21px; color: var(--brand-bright); margin-top: 6px; }
  .rule { width: 600px; height: 1px; background: var(--rule-dark); margin: 10px auto; }
  .services { font-family: "Roboto Condensed", sans-serif; font-size: 18.5px; line-height: 1.45; color: var(--on-dark); padding: 0 40px; }
  .services .sep { color: var(--brand-bright); padding: 0 4px; }
</style>
</head>
<body>
  <section class="card card-front">
    <div class="person">
      <div class="person-name">Elena <span class="surname">Varga</span></div>
      <div class="person-role">Director</div>
    </div>
    <div class="divider"></div>
    <div class="contact">
      <div class="contact-row plain">27 Alder Lane,</div>
      <div class="contact-row plain">London, UK, E2 7QX</div>
      <div class="contact-row">
        <svg viewBox="0 0 24 24"><path d="M6.6 10.8a15 15 0 0 0 6.6 6.6l2.2-2.2c.3-.3.7-.4 1-.2 1.1.4 2.3.6 3.6.6.6 0 1 .4 1 1V20c0 .6-.4 1-1 1A17 17 0 0 1 3 4c0-.6.4-1 1-1h3.5c.6 0 1 .4 1 1 0 1.3.2 2.5.6 3.6.1.3 0 .7-.2 1z"/></svg>
        (020) 555-0147
      </div>
      <div class="contact-row">
        <svg viewBox="0 0 24 24"><path d="M2 5h20v14H2zm2 2v.5l8 5 8-5V7z"/></svg>
        info@talkbridge-demo.co.uk
      </div>
      <div class="contact-row">
        <svg viewBox="0 0 24 24"><circle cx="12" cy="12" r="10"/></svg>
        www.<span class="web-strong">talkbridge-demo</span>.co.uk
      </div>
    </div>
    <div class="brand">
      <span class="brand-dot"></span>
      <span class="brand-name">TalkBridge</span>
    </div>
  </section>

  <section class="card card-back">
    <div class="back-brand">
      <span class="brand-dot"></span>
      <span class="brand-name">TalkBridge</span>
    </div>
    <div class="services-title">Our Services</div>
    <div class="tagline">We offer highly customized coaching sessions and self-study content.</div>
    <div class="rule"></div>
    <p class="services">
      Face to face language coaching sessions<span class="sep">|</span>On-line language coaching sessions<br>
      Personalized Newsletters for self-learners<span class="sep">|</span>Language Learning Techniques Workshops<br>
      Mindful Learning Workshops<span class="sep">|</span>Access to premium content, resources.
    </p>
  </section>
</body>
</html>
```